Direct Mail Postcard for new client solicitation

I need a postcard designed to market our full service accounting and financial services firm to local companies.

Our firm specializes in outsourced accounting and finance - we do everything from book keeping all the way up to financial oversight. We prefer to work on a flat fee recurring revenue basis rather than a traditional hourly fee. We also bring our own privately developed software to assist with the process. This software is proprietary in nature and not available elsewhere.

This card should convey:
1. Transferring financial headaches to a qualified company.
2. Stable access to help.
3. Cost savings.
4. A comprehensive package that allows for the client to take as much or as little as they would like.

I have attached our logo as a starting point. Feel free to engage us with questions and for guidance.

The company name is BrightLedgerCo.

Target Market(s)

the target market for this project is small businesses in the chicago area (our test market) with annual revenues between 5 and 10 Million dollars

Industry/Entity Type

Accounting

Font styles to use
Serif
Sans Serif

Requirements
Must have
• The project must convey the idea that we are taking administrative burdens and headaches from the client. The idea is that they are outsourcing their back office accounting functions to us while still retaining overall control of the process. The card must convey this concept somehow.
• We are also working on copy - since we are accountants and basically as boring as watching paint dry we are struggling a bit. Feel free to take a stab at copy as well. Keep in mind - we do not need to say alot - ideally we would say in essence "outsource your finance and accounting work to us for a reasonable fixed price".
Should not have
• We are reworking our website as well. The little orange guys and in fact the entire copy will be changing over the next few weeks. We would prefer to avoid using that motif for the card.

```html
<!DOCTYPE html>
<html lang="en">
<head>
<meta charset="utf-8">
<title>BrightLedgerCo Postcard</title>
<link rel="stylesheet" href="https://fonts.googleapis.com/css2?family=Arimo:wght@400;700&display=swap">
<style>
  :root {
    --bg: #ece9e4;
    --card: #ffffff;
    --navy: #0b5878;
    --green: #1f9447;
    --lime: #c9da2c;
    --tick: #f3b62a;
    --ink: #ffffff;
    --rule: #a9a9a9;
    --stamp: #222222;
    --photo-a: #e9e4d8;
    --photo-b: #b9ac92;
  }
  * { box-sizing: border-box; margin: 0; padding: 0; }
  html, body { width: 1200px; height: 800px; overflow: hidden; }
  body {
    background: var(--bg);
    font-family: "Arimo", Arial, sans-serif;
    position: relative;
  }
  .postcard {
    position: absolute;
    top: 210px;
    width: 570px;
    height: 380px;
    background: var(--card);
    box-shadow: 0 2px 8px rgba(0,0,0,0.18);
  }
  .postcard--message { left: 20px; }
  .postcard--services { left: 610px; }

  /* Message side */
  .message-panel {
    position: absolute;
    left: 14px; top: 14px;
    width: 344px; height: 352px;
    background: var(--navy);
    color: var(--ink);
    padding: 34px 28px 0 52px;
  }
  .message-title {
    font-size: 27px;
    font-weight: 400;
    line-height: 1.1;
  }
  .message-lede {
    font-size: 12.5px;
    line-height: 1.3;
    margin-top: 4px;
  }
  .message-body {
    font-size: 12.5px;
    line-height: 1.32;
    margin-top: 16px;
  }
  .accent-rule {
    position: absolute;
    left: 358px; top: 14px;
    width: 4px; height: 352px;
    background: var(--lime);
  }
  .photo-area {
    position: absolute;
    left: 362px; top: 14px;
    width: 194px; height: 352px;
    background: linear-gradient(160deg, var(--photo-a) 0%, #d8cfbd 55%, var(--photo-b) 100%);
  }

  /* Services side */
  .services-shape {
    position: absolute;
    left: 14px; top: 14px;
  }
  .services-copy {
    position: absolute;
    left: 36px; top: 34px;
    width: 300px;
    color: var(--ink);
    font-size: 16.5px;
    line-height: 1.2;
  }
  .services-list {
    list-style: none;
    margin: 1px 0 0 0;
  }
  .services-list li {
    display: flex;
    align-items: center;
    gap: 4px;
  }
  .tick { width: 17px; height: 14px; flex: none; }
  .services-tagline { margin-top: 18px; }

  .stamp-box {
    position: absolute;
    right: 44px; top: 40px;
    width: 52px; height: 62px;
    border: 1.5px solid var(--stamp);
  }
  .address-lines {
    position: absolute;
    left: 378px; top: 160px;
    width: 150px;
  }
  .address-lines span {
    display: block;
    height: 24px;
    border-bottom: 1px solid var(--rule);
  }
</style>
</head>
<body>

<section class="postcard postcard--message">
  <div class="message-panel">
    <h1 class="message-title">Finance, simplified</h1>
    <p class="message-lede">Hand off those financial chores without losing control of your books.</p>
    <p class="message-body">BrightLedgerCo, a finance and consulting firm, provides outsourced financial services that is revolutionizing how businesses work. Proprietary tools and modern methods mean we provide a complete solution to all your accounting and finance issues! Now you can move just the issues you want - at prices you can afford.</p>
  </div>
  <div class="accent-rule"></div>
  <div class="photo-area" role="img" aria-label="Photo of open ledger books, papers and a pencil on a desk"></div>
</section>

<section class="postcard postcard--services">
  <svg class="services-shape" width="352" height="352" viewBox="0 0 352 352" aria-hidden="true">
    <polygon points="0,0 326,0 296,352 0,352" fill="var(--green)"/>
    <polygon points="326,0 350,0 318,352 296,352" fill="var(--navy)"/>
  </svg>

  <div class="services-copy">
    <p>We can help with</p>
    <ul class="services-list">
      <li><svg class="tick" viewBox="0 0 17 14" aria-hidden="true"><path d="M1 7.5 L6 12.5 L16 1.5" fill="none" stroke="var(--tick)" stroke-width="3.2" stroke-linecap="round" stroke-linejoin="round"/></svg>Financial management</li>
      <li><svg class="tick" viewBox="0 0 17 14" aria-hidden="true"><path d="M1 7.5 L6 12.5 L16 1.5" fill="none" stroke="var(--tick)" stroke-width="3.2" stroke-linecap="round" stroke-linejoin="round"/></svg>Accounting</li>
      <li><svg class="tick" viewBox="0 0 17 14" aria-hidden="true"><path d="M1 7.5 L6 12.5 L16 1.5" fill="none" stroke="var(--tick)" stroke-width="3.2" stroke-linecap="round" stroke-linejoin="round"/></svg>Book keeping</li>
      <li><svg class="tick" viewBox="0 0 17 14" aria-hidden="true"><path d="M1 7.5 L6 12.5 L16 1.5" fill="none" stroke="var(--tick)" stroke-width="3.2" stroke-linecap="round" stroke-linejoin="round"/></svg>Forecasting</li>
      <li><svg class="tick" viewBox="0 0 17 14" aria-hidden="true"><path d="M1 7.5 L6 12.5 L16 1.5" fill="none" stroke="var(--tick)" stroke-width="3.2" stroke-linecap="round" stroke-linejoin="round"/></svg>Reporting</li>
      <li><svg class="tick" viewBox="0 0 17 14" aria-hidden="true"><path d="M1 7.5 L6 12.5 L16 1.5" fill="none" stroke="var(--tick)" stroke-width="3.2" stroke-linecap="round" stroke-linejoin="round"/></svg>Bank management</li>
      <li><svg class="tick" viewBox="0 0 17 14" aria-hidden="true"><path d="M1 7.5 L6 12.5 L16 1.5" fill="none" stroke="var(--tick)" stroke-width="3.2" stroke-linecap="round" stroke-linejoin="round"/></svg>Fund raising</li>
      <li><svg class="tick" viewBox="0 0 17 14" aria-hidden="true"><path d="M1 7.5 L6 12.5 L16 1.5" fill="none" stroke="var(--tick)" stroke-width="3.2" stroke-linecap="round" stroke-linejoin="round"/></svg>Business transition planning</li>
      <li><svg class="tick" viewBox="0 0 17 14" aria-hidden="true"><path d="M1 7.5 L6 12.5 L16 1.5" fill="none" stroke="var(--tick)" stroke-width="3.2" stroke-linecap="round" stroke-linejoin="round"/></svg>Tax compliance</li>
    </ul>
    <p class="services-tagline">If you have headaches we have solutions!</p>
  </div>

  <div class="stamp-box" aria-hidden="true"></div>
  <div class="address-lines" aria-hidden="true">
    <span></span><span></span><span></span><span></span><span></span>
  </div>
</section>

</body>
</html>
```